Acupuncture business needs business card design

I need a business card for an acupuncture clinic called "Summit Wellpath"
It will need the following details:
My name: Marcus Thelwick
Acupuncturist
Member KPTG
BVF Treatment Provider
Ph numbers: 482 1358 027 514 3820
Email: marcus@swpath.example.nz
On the back it will need a table with 2 columns for appointments, one column for time and one for date.

Industry/Entity Type

Clinic

Contact Information for Business Card

Marcus Thelwick
Acupuncturist
Member KPTG
BVF Treatment Provider
Email: marcus@swpath.example.nz

Requirements
Must have
• Marcus Thelwick
• Acupuncturist
• Member KPTG
• BVF Treatment Provider
• Ph numbers: 482 1358 027 514 3820
• Email: marcus@swpath.example.nz
• On the back it will need a table with 2 columns for appointments, one column for time and one for date.

```html
<!DOCTYPE html>
<html lang="en">
<head>
<meta charset="utf-8">
<title>Summit Wellpath – Business Card</title>
<link rel="stylesheet" href="https://fonts.googleapis.com/css2?family=Exo+2:wght@400;500;600&display=swap">
<style>
  :root {
    --page-bg: #e6e6e4;
    --card-white: #ffffff;
    --card-grey: #e4e5e6;
    --teal: #2b7f99;
    --teal-dark: #23718a;
    --sky: #2aaee3;
    --ink: #333b40;
    --muted: #59646b;
    --line-light: rgba(255,255,255,.55);
  }
  * { box-sizing: border-box; margin: 0; padding: 0; }
  html, body { width: 1200px; height: 800px; overflow: hidden; }
  body {
    background: var(--page-bg);
    font-family: "Exo 2", sans-serif;
    position: relative;
  }
  .card {
    position: absolute;
    box-shadow: 0 6px 18px rgba(0,0,0,.18);
    overflow: hidden;
  }

  /* Front */
  .card-front {
    left: 80px; top: 240px; width: 560px; height: 320px;
    background: radial-gradient(ellipse at 40% 40%, var(--card-white) 0%, var(--card-grey) 100%);
  }
  .front-curves { position: absolute; inset: 0; }
  .brand {
    position: absolute; left: 30px; top: 98px; width: 220px;
    text-align: center; color: var(--sky);
  }
  .brand-dot {
    width: 18px; height: 18px; border-radius: 50%;
    border: 3px solid var(--teal); margin: 0 auto 4px;
  }
  .brand-name { font-size: 27px; font-weight: 500; line-height: 1.05; letter-spacing: .2px; }
  .brand-tagline {
    font-size: 8px; letter-spacing: 3.2px; color: var(--teal);
    text-transform: uppercase; margin-top: 2px;
  }
  .holder { position: absolute; left: 320px; top: 100px; }
  .holder-name {
    font-size: 19px; font-weight: 500; color: var(--teal);
    letter-spacing: 1.2px; text-transform: uppercase; line-height: 1.2;
  }
  .holder-role { font-size: 10.5px; font-weight: 500; color: var(--ink); margin-top: 2px; }
  .holder-affiliations { list-style: none; font-size: 9.5px; color: var(--muted); margin-top: 3px; }
  .holder-affiliations li { line-height: 13px; }
  .contacts {
    position: absolute; left: 320px; top: 212px;
    list-style: none; font-size: 9.5px; color: var(--muted);
  }
  .contacts li { display: flex; align-items: center; gap: 6px; height: 16px; }
  .contacts svg { width: 9px; height: 9px; fill: var(--teal); flex: none; }

  /* Back */
  .card-back {
    left: 720px; top: 120px; width: 320px; height: 560px;
    background: var(--teal);
    display: flex; flex-direction: column; align-items: center;
    padding-top: 70px;
    color: var(--card-white);
  }
  .back-dot {
    width: 80px; height: 80px; border-radius: 50%;
    border: 11px solid var(--card-white); margin-bottom: 16px;
  }
  .back-name { font-size: 23px; font-weight: 500; }
  .appointments-title {
    margin-top: 34px; font-size: 11px; letter-spacing: 3px;
    text-transform: uppercase;
  }
  .appointments {
    margin-top: 10px; width: 240px;
    border-collapse: collapse; font-size: 11px;
  }
  .appointments th {
    font-weight: 500; text-transform: uppercase; letter-spacing: 1.5px;
    height: 24px; border-bottom: 1.5px solid var(--card-white);
  }
  .appointments td {
    height: 30px; border-bottom: 1px solid var(--line-light);
  }
  .appointments th + th, .appointments td + td { border-left: 1px solid var(--line-light); }
</style>
</head>
<body>
  <section class="card card-front">
    <svg class="front-curves" viewBox="0 0 560 320" aria-hidden="true">
      <path d="M238 0 C320 70 310 235 140 320 L170 320 C335 232 345 75 262 0 Z" fill="var(--teal-dark)"/>
      <path d="M292 90 C305 190 250 270 150 320 L192 320 C290 262 320 175 292 90 Z" fill="var(--sky)"/>
    </svg>

    <div class="brand">
      <div class="brand-dot"></div>
      <div class="brand-name">Summit Wellpath</div>
      <div class="brand-tagline">Acupuncture Physiotherapy</div>
    </div>

    <div class="holder">
      <div class="holder-name">Marcus Thelwick</div>
      <div class="holder-role">Acupuncturist</div>
      <ul class="holder-affiliations">
        <li>Member KPTG</li>
        <li>BVF Treatment Provider</li>
      </ul>
    </div>

    <ul class="contacts">
      <li><svg viewBox="0 0 10 10"><rect x="2.5" y="0" width="5" height="10" rx="1"/></svg>482 1358</li>
      <li><svg viewBox="0 0 10 10"><path d="M2 0 L4 2.5 L3 4 C4 6 5 7 6 7 L7.5 6 L10 8 L8.5 10 C4 10 0 6 0 1.5 Z"/></svg>027 514 3820</li>
      <li><svg viewBox="0 0 10 10"><rect x="0" y="1.5" width="10" height="7" rx="1"/></svg>marcus@swpath.example.nz</li>
      <li><svg viewBox="0 0 10 10"><circle cx="5" cy="5" r="5"/></svg>www.swpath.example.nz</li>
      <li><svg viewBox="0 0 10 10"><path d="M5 0 C2 0 1 2.2 1 3.8 C1 6.5 5 10 5 10 C5 10 9 6.5 9 3.8 C9 2.2 8 0 5 0 Z"/></svg>14 Harbour Lane, Level 2 | NZ</li>
    </ul>
  </section>

  <section class="card card-back">
    <div class="back-dot"></div>
    <div class="back-name">Summit Wellpath</div>
    <div class="appointments-title">Appointments</div>
    <table class="appointments">
      <thead><tr><th>Date</th><th>Time</th></tr></thead>
      <tbody>
        <tr><td></td><td></td></tr>
        <tr><td></td><td></td></tr>
        <tr><td></td><td></td></tr>
        <tr><td></td><td></td></tr>
        <tr><td></td><td></td></tr>
      </tbody>
    </table>
  </section>
</body>
</html>
```